Letterhead Design Project

Professional but modern letterhead.

Target Market(s)

mining companies

Industry/Entity Type

It Professional

Colors

Designer to choose colors to be used in the design.

```html
<!DOCTYPE html>
<html lang="en">
<head>
<meta charset="utf-8">
<title>VORAN Letterhead</title>
<link href="https://fonts.googleapis.com/css2?family=Open+Sans:wght@400;600&display=swap" rel="stylesheet">
<style>
  :root {
    --brand-blue: #0432d8;
    --ink: #1e1e1e;
    --paper: #ffffff;
  }
  * { margin: 0; padding: 0; box-sizing: border-box; }
  html, body {
    width: 849px;
    height: 1200px;
    overflow: hidden;
    background: var(--paper);
  }
  .letterhead {
    position: relative;
    width: 849px;
    height: 1200px;
    background: var(--paper);
    font-family: "Open Sans", Arial, sans-serif;
    color: var(--ink);
  }
  .brand {
    position: absolute;
    left: 68px;
    top: 150px;
    display: flex;
    align-items: center;
    gap: 14px;
  }
  .brand-mark {
    width: 30px;
    height: 30px;
    background: var(--brand-blue);
  }
  .brand-name {
    font-weight: 600;
    font-size: 52px;
    letter-spacing: 1px;
    color: var(--brand-blue);
    line-height: 1;
  }
  .contact {
    position: absolute;
    top: 70px;
    font-size: 15.5px;
    line-height: 24px;
    list-style: none;
  }
  .contact-left { left: 451px; }
  .contact-right { left: 640px; }
  .contact-item {
    display: flex;
    align-items: flex-start;
    gap: 7px;
    margin-bottom: 2px;
  }
  .contact-item svg {
    flex: 0 0 16px;
    width: 16px;
    height: 16px;
    margin-top: 4px;
  }
  .contact-item.tight { margin-bottom: 0; }
  .footer-wave {
    position: absolute;
    left: 0;
    bottom: 0;
    width: 849px;
    height: 246px;
    display: block;
  }
</style>
</head>
<body>
<div class="letterhead">

  <div class="brand">
    <span class="brand-mark"></span>
    <span class="brand-name">VORAN</span>
  </div>

  <ul class="contact contact-left">
    <li class="contact-item">
      <svg viewBox="0 0 16 16" aria-hidden="true"><circle cx="8" cy="8" r="8" fill="#1e1e1e"/><path d="M3.5 8.2 8 4.2l4.5 4v3.8h-3V9.6h-3V12h-3z" fill="#fff"/></svg>
      <span>Suite # 418, Kell Bldg<br>NY 60418</span>
    </li>
    <li class="contact-item">
      <svg viewBox="0 0 16 16" aria-hidden="true"><circle cx="8" cy="8" r="8" fill="#1e1e1e"/><path d="M5.2 3.8c.6-.4 1.2-.2 1.5.3l.8 1.3c.3.5.1 1-.3 1.3l-.5.4c.4 1 1.2 1.9 2.2 2.4l.4-.5c.3-.4.9-.5 1.3-.2l1.3.8c.5.3.6 1 .2 1.5-.8.9-1.9 1.1-3 .6C6.9 10.6 5.2 8.8 4.4 6.7c-.4-1.1-.1-2.2.8-2.9z" fill="#fff"/></svg>
      <span>555-214-0937</span>
    </li>
  </ul>

  <ul class="contact contact-right">
    <li class="contact-item tight">
      <svg viewBox="0 0 16 16" aria-hidden="true"><circle cx="8" cy="8" r="8" fill="#1e1e1e"/><rect x="5" y="3.5" width="6" height="3" fill="#fff"/><rect x="4" y="6.8" width="8" height="5.5" rx="1" fill="#fff"/><rect x="5.5" y="8.3" width="5" height="2.5" fill="#1e1e1e"/></svg>
      <span>555-381-6042</span>
    </li>
    <li class="contact-item tight">
      <svg viewBox="0 0 16 16" aria-hidden="true"><circle cx="8" cy="8" r="8" fill="#1e1e1e"/><rect x="3.8" y="5" width="8.4" height="6" fill="#fff"/><path d="M3.8 5 8 8.5 12.2 5" fill="none" stroke="#1e1e1e" stroke-width="1"/></svg>
      <span>hello@voran.com</span>
    </li>
    <li class="contact-item tight">
      <svg viewBox="0 0 16 16" aria-hidden="true"><circle cx="8" cy="8" r="8" fill="#1e1e1e"/><g fill="none" stroke="#fff" stroke-width="1"><circle cx="8" cy="8" r="4.8"/><ellipse cx="8" cy="8" rx="2.2" ry="4.8"/><path d="M3.2 8h9.6M4 5.6h8M4 10.4h8"/></g></svg>
      <span>www.voran.com</span>
    </li>
  </ul>

  <svg class="footer-wave" viewBox="0 0 827 240" preserveAspectRatio="none" aria-hidden="true">
    <path d="M0 131 C60 200 180 215 330 185 C480 150 640 60 827 39 L827 240 L0 240 Z" fill="var(--brand-blue)"/>
    <path d="M8 189 C120 238 300 240 450 186 C600 132 720 66 827 54 L827 62 C720 76 600 142 450 196 C300 250 120 246 8 189 Z" fill="var(--paper)"/>
  </svg>

</div>
</body>
</html>
```